Course Graduation Certificate

This project is not for a flyer but instead for the creation of a course graduation certificate. The final certificate needs to include the Marrow Summit Aviation Academy logo and the text stating as follows:
Certifies that ___________________________ has satisfactorily completed the course of _______________________________ on ________________________________
I would also like to include some type of gold seal of completion as well as a place to sign my name and credentials at the bottom of the certificate
I have included the Marrow Summit Aviation Academy logo as well as three other certificate examples for you to work from.
Target Market(s)
Students completing a certification course and receiving a certificate

```html
<!DOCTYPE html>
<html lang="en">
<head>
<meta charset="utf-8">
<title>Certificate of Completion – Marrow Summit Aviation Academy</title>
<link rel="stylesheet" href="https://fonts.googleapis.com/css2?family=Cinzel:wght@400;600&family=Tinos:wght@400;700&display=swap">
<style>
  :root {
    --backdrop: #595959;
    --paper: #ffffff;
    --paper-tint: #f6f6f7;
    --frame-grey: #9a9b9d;
    --ornament-grey: #b9babc;
    --title-blue: #2b5675;
    --ink: #1a1a1a;
    --field-grey: #7b7b7b;
    --brand-blue: #1f5fae;
    --gold-light: #f3d77a;
    --gold-deep: #b48a2a;
  }
  * { margin: 0; padding: 0; box-sizing: border-box; }
  html, body { width: 1200px; height: 874px; overflow: hidden; }
  body { background: var(--backdrop); position: relative; }

  .certificate {
    position: absolute; left: 99px; top: 100px;
    width: 1001px; height: 675px;
    background: radial-gradient(ellipse at center, var(--paper) 55%, var(--paper-tint) 100%);
  }
  .frame-outer {
    position: absolute; left: 20px; top: 18px; width: 963px; height: 654px;
    border: 3px solid var(--frame-grey);
  }
  .frame-inner {
    position: absolute; left: 26px; top: 24px; width: 951px; height: 642px;
    border: 1px solid var(--frame-grey);
  }
  .border-ornament {
    position: absolute; left: 30px; top: 28px; width: 943px; height: 634px;
    border: 30px solid var(--ornament-grey);
    opacity: 0.75;
  }
  .border-ornament::after {
    content: ""; position: absolute; inset: 4px;
    border: 1px solid var(--paper);
  }

  .line { position: absolute; left: 0; right: 0; text-align: center; }
  .title {
    top: 92px; font-family: "Cinzel", serif; font-weight: 600;
    font-size: 56px; letter-spacing: 14px; color: var(--title-blue);
    padding-left: 14px;
  }
  .subtitle {
    top: 150px; font-family: "Cinzel", serif; font-weight: 600;
    font-size: 36px; letter-spacing: 5px; color: var(--title-blue);
  }
  .divider {
    position: absolute; left: 441px; width: 118px; height: 1px;
    background: var(--frame-grey);
  }
  .divider span {
    position: absolute; left: 41px; top: -5px; width: 36px; height: 11px;
    background: var(--ornament-grey); border-radius: 5px;
  }
  .label {
    font-family: "Cinzel", serif; font-weight: 600; font-size: 20px;
    color: var(--ink); letter-spacing: 0.5px;
  }
  .field {
    font-family: "Tinos", serif; font-weight: 700; font-size: 18px;
    color: var(--field-grey); letter-spacing: 0.5px;
  }

  .seal {
    position: absolute; left: 173px; top: 497px; width: 98px; height: 98px;
    border-radius: 50%;
    background: radial-gradient(circle at 40% 35%, var(--gold-light), var(--gold-deep) 75%);
  }
  .academy-name {
    position: absolute; left: 405px; top: 528px; width: 180px;
    text-align: center; font-family: "Tinos", serif; font-weight: 700;
    font-size: 17px; line-height: 1.15; color: var(--brand-blue);
  }

  .signature-area { position: absolute; left: 682px; top: 494px; width: 189px; }
  .signature-mark {
    height: 34px; width: 130px; margin: 0 auto;
    background: linear-gradient(90deg, transparent, #d8d8d8 20%, #d8d8d8 80%, transparent);
    opacity: 0.6; border-radius: 4px;
  }
  .signature-rule { height: 1px; background: var(--ink); margin-top: 1px; }
  .signer { text-align: center; font-family: "Tinos", serif; color: var(--ink); }
  .signer-name { font-weight: 700; font-size: 14px; margin-top: 10px; }
  .signer-role { font-size: 9px; line-height: 1.25; }
</style>
</head>
<body>
  <main class="certificate">
    <div class="frame-outer"></div>
    <div class="frame-inner"></div>
    <div class="border-ornament" role="img" aria-label="Decorative guilloche scalloped border"></div>

    <h1 class="line title">Certificate</h1>
    <h2 class="line subtitle">of Completion</h2>

    <div class="divider" style="top:230px" role="img" aria-label="Ornamental divider"><span></span></div>

    <p class="line label" style="top:250px">Certifies that</p>
    <p class="line field" style="top:282px">NAME GOES HERE</p>
    <p class="line label" style="top:326px">Has Satisfactorily Completed The Course Of</p>
    <p class="line field" style="top:357px">STRATUS 300, 135 INHC</p>
    <p class="line label" style="top:396px">Conferred On</p>
    <p class="line field" style="top:427px">15TH DAY OF FEBRUARY 2025</p>

    <div class="divider" style="top:474px" role="img" aria-label="Ornamental divider"><span></span></div>

    <div class="seal" role="img" aria-label="Gold seal of completion"></div>

    <p class="academy-name">Marrow Summit Aviation Academy</p>

    <div class="signature-area">
      <div class="signature-mark" role="img" aria-label="Handwritten signature"></div>
      <div class="signature-rule"></div>
      <div class="signer">
        <p class="signer-name">Nolan R. Ashby</p>
        <p class="signer-role">Certified Flight Instructor</p>
        <p class="signer-role">Certificate#: 3917462CFI</p>
      </div>
    </div>
  </main>
</body>
</html>
```